Velvet corsaro

I want a business card design. the company is an infrastructure development company.

Target Market(s)

Government
real estate investors
real estate clients

Industry/Entity Type

Business

```html
<!DOCTYPE html>
<html lang="en">
<head>
<meta charset="utf-8">
<title>Velvet Corsaro – Business Card</title>
<link href="https://fonts.googleapis.com/css2?family=Play:wght@400;700&display=swap" rel="stylesheet">
<style>
  :root {
    --red: #ec3237;
    --blue: #00aeef;
    --text-blue: #0d9ee0;
    --white: #ffffff;
    --ink: #111111;
    --backdrop: #e9e6e2;
  }
  * { margin: 0; padding: 0; box-sizing: border-box; }
  html, body { width: 1200px; height: 658px; overflow: hidden; }
  body {
    background: var(--backdrop);
    font-family: "Play", sans-serif;
    position: relative;
  }
  .card {
    position: absolute;
    top: 100px;
    width: 260px;
    height: 440px;
    background: var(--white);
    overflow: hidden;
    box-shadow: 0 6px 18px rgba(0,0,0,0.18);
  }
  /* ---------- back card ---------- */
  .card--back { left: 320px; }
  .card--back .edge {
    position: absolute; top: 0; right: 0; width: 10px; height: 100%;
    background: linear-gradient(to right, var(--red) 0 50%, var(--blue) 50% 100%);
  }
  .brand-block {
    position: absolute; top: 48px; left: 0; right: 10px;
    display: flex; align-items: center; justify-content: center; gap: 8px;
  }
  .brand-square { width: 16px; height: 16px; background: var(--red); }
  .brand-name {
    font-weight: 700; font-size: 22px; color: var(--red);
    letter-spacing: 1px; text-transform: uppercase;
  }
  .section-tab {
    position: absolute; left: 0; height: 28px; width: 200px;
  }
  .tab-shape { position: absolute; inset: 0; }
  .section-tab span {
    position: relative; display: block; line-height: 28px;
    padding-left: 38px; color: var(--white); font-weight: 700; font-size: 15px;
  }
  .tab-company { top: 150px; }
  .tab-mine { top: 290px; }
  .detail {
    position: absolute; right: 24px; text-align: right;
    color: var(--text-blue); font-size: 11px; line-height: 1.35;
  }
  .detail-company { top: 188px; width: 220px; }
  .detail-company .web { font-size: 13px; font-weight: 700; }
  .detail-mine { top: 326px; width: 220px; text-align: center; right: 18px; }
  .detail-mine .person { font-size: 14px; }
  .detail-mine .role { font-size: 13px; margin-bottom: 2px; }
  .detail-mine .email { font-size: 13px; }
  /* ---------- front card ---------- */
  .card--front { left: 620px; }
  .front-brand {
    position: absolute; top: 70px; left: 0; right: 0;
    display: flex; align-items: center; justify-content: center; gap: 8px;
  }
  .front-brand .brand-name { font-size: 24px; }
  .service-panel { position: absolute; left: 0; top: 175px; width: 260px; height: 265px; }
  .panel-shape { position: absolute; inset: 0; }
  .service-list {
    position: relative; list-style: none; padding: 40px 0 0 12px;
  }
  .service-list li {
    display: flex; align-items: center; gap: 6px;
    color: var(--white); font-weight: 700; font-size: 16px; line-height: 25px;
  }
  .tick { width: 18px; height: 18px; flex: none; }
</style>
</head>
<body>

<section class="card card--back" aria-label="Card back">
  <div class="edge"></div>
  <div class="brand-block">
    <div class="brand-square"></div>
    <div class="brand-name">Velvet Corsaro</div>
  </div>

  <div class="section-tab tab-company">
    <svg class="tab-shape" width="200" height="28" viewBox="0 0 200 28"><polygon points="0,0 186,0 200,14 186,28 0,28" fill="var(--red)"/></svg>
    <span>Company Details</span>
  </div>
  <div class="detail detail-company">
    <p>14, Marlow Crescent, Off Harbour Link Road,</p>
    <p>Eastfield Lagos, Nigeria</p>
    <p>+2341555010, +2347005550123</p>
    <p class="web">www.velvetcorsaro.com</p>
  </div>

  <div class="section-tab tab-mine">
    <svg class="tab-shape" width="200" height="28" viewBox="0 0 200 28"><polygon points="0,0 186,0 200,14 186,28 0,28" fill="var(--red)"/></svg>
    <span>My Details</span>
  </div>
  <div class="detail detail-mine">
    <p class="person">Kemi Adeyemi</p>
    <p class="role">MD.</p>
    <p>+234 8005550142, +234 7005550187</p>
    <p class="email">kemi@velvetcorsaro.com</p>
  </div>
</section>

<section class="card card--front" aria-label="Card front">
  <div class="front-brand">
    <div class="brand-square"></div>
    <div class="brand-name">Velvet Corsaro</div>
  </div>

  <div class="service-panel">
    <svg class="panel-shape" width="260" height="265" viewBox="0 0 260 265">
      <polygon points="0,26 44,26 52,10 140,10 148,2 214,2 222,10 260,10 260,265 0,265" fill="var(--red)"/>
      <polygon points="0,32 46,32 54,16 142,16 150,8 212,8 220,16 260,16 260,188 0,218" fill="var(--blue)"/>
    </svg>
    <ul class="service-list">
      <li><svg class="tick" viewBox="0 0 16 16"><path d="M1 9 L6 14 L15 2" fill="none" stroke="var(--ink)" stroke-width="3"/></svg>Building Engineering</li>
      <li><svg class="tick" viewBox="0 0 16 16"><path d="M1 9 L6 14 L15 2" fill="none" stroke="var(--ink)" stroke-width="3"/></svg>Flood Risk Management</li>
      <li><svg class="tick" viewBox="0 0 16 16"><path d="M1 9 L6 14 L15 2" fill="none" stroke="var(--ink)" stroke-width="3"/></svg>Canal and Waterway</li>
      <li><svg class="tick" viewBox="0 0 16 16"><path d="M1 9 L6 14 L15 2" fill="none" stroke="var(--ink)" stroke-width="3"/></svg>Geospatial Solutions</li>
      <li><svg class="tick" viewBox="0 0 16 16"><path d="M1 9 L6 14 L15 2" fill="none" stroke="var(--ink)" stroke-width="3"/></svg>Highway Engineering</li>
      <li><svg class="tick" viewBox="0 0 16 16"><path d="M1 9 L6 14 L15 2" fill="none" stroke="var(--ink)" stroke-width="3"/></svg>Environmental</li>
    </ul>
  </div>
</section>

</body>
</html>
```